依頼詳細
・商品が増えたので新商品の案内 ギフト商品の紹介のチラシ(金額は入れません。)
・「こはるフルーツソース2本セット」を目玉として大きめに表示してください。
・商品の色を前面に出したデザインによる商品紹介
・文章はなるべく入れないで写真を強調した、シンプルでわかりやすいデザイン
・食品関連ギフトのチラシの作成経験者歓迎
・真空低温調理によるジャム製造のため、酸化も少なく、色が鮮やかなジャムに仕上がっています。
・自社農園産の果物を中心に、宮崎県産果物のみを使用。
・通常の手作業では実現できない品質をご提供することができます。
記載項目
「宝石のようなトロピカルジャム」という文言を必ず使用してください。

・こはるフルーツソース2本セット
「北海道産てんさい糖と宮崎県産フルーツのみを煮詰めたこだわりのソース」
内容:マンゴーソース  145g
パッションフルーツソース 145g

・こはるフルーツジャム6個セット
内容:マンゴージャム 150g
日向夏マーマレード 150g
きんかんマーマレード 150g
パイナップルジャム 150g
ブルーベリージャム 150g
パパイアジャム  150g

・こはるフルーツミニジャム6個セット
内容:マンゴージャム 50g
日向夏マーマレード 50g
きんかんマーマレード 50g
パイナップルジャム 50g
ブルーベリージャム 50g
パパイアジャム 50g

桐原白浜果樹株式会社
〒876-2231 宮崎県宮崎市桜丘町岩瀬2264番地
電話番号: 0985-47-2291
FAX:  0985-47-3356
サイズ
A4
ページ数
片面
希望イメージ
シンプル 複雑
単色 カラフル
暗い 明るい
日常 高級
遊び心 厳粛
未来的 伝統的
女性的 男性的
希望する色
納品ファイル
補足説明
■ 選んだ理由

シンプルで、しかも美味しさと高級感が伝わるようなデザインで、社内アンケートの結果一番評価が高かったので決めさせていただきました。

■ 提案者全員のお礼・コメント

たくさんのご提案をしていただき、選考には時間が
かかってしまい申し訳ありませんでした。どの方も素晴らしく、選ぶのにすごく悩みましたが、社内で検討し、一人の方を選ばせていただきました。
今回、初めて利用させていただきましたが、皆様のような素晴らしいデザイナーさんがいらっしゃるということが実感できましたので、また
利用させていただきたいと考えておりますので、今後ともどうぞよろしくお願いいたします。
本当にありがとうございました。

```html
<!DOCTYPE html>
<html lang="ja">
<head>
<meta charset="utf-8">
<title>こはるフルーツ ギフトのご案内</title>
<link href="https://fonts.googleapis.com/css2?family=Shippori+Mincho:wght@400;600&family=Noto+Sans+JP:wght@400;500&family=Great+Vibes&display=swap" rel="stylesheet">
<style>
:root{
  --paper:#ffffff;
  --gold:#b48a35;
  --gold-light:#e6c98a;
  --ink:#2f2a24;
  --muted:#5c544a;
  --rule:#c9b27c;
}
*{margin:0;padding:0;box-sizing:border-box}
html,body{width:863px;height:1200px;overflow:hidden;background:var(--paper)}
.flyer{position:relative;width:863px;height:1200px;background:var(--paper);font-family:"Noto Sans JP",sans-serif;color:var(--ink);overflow:hidden}
.hero-photo{position:absolute;left:0;top:0;width:863px;height:580px;
  background:
   linear-gradient(180deg,rgba(255,255,255,0) 0%,rgba(255,255,255,0) 62%,#ffffff 92%),
   radial-gradient(ellipse 120px 230px at 245px 240px,#d9a233 0%,rgba(217,162,51,0) 70%),
   radial-gradient(ellipse 115px 225px at 410px 240px,#f0b52a 0%,rgba(240,181,42,0) 70%),
   linear-gradient(90deg,#f6eedc 0%,#efe0bd 45%,#5a4520 72%,#1e160c 100%)}
.gift-word{position:absolute;left:28px;top:18px;font-family:"Great Vibes",cursive;font-size:72px;color:#fff;opacity:.85}
.headline{position:absolute;left:470px;top:70px;font-family:"Shippori Mincho",serif;font-weight:600;color:var(--gold-light);font-size:44px;line-height:1.4}
.headline span{display:block}
.headline span:last-child{padding-left:14px}
.sauce-photo{position:absolute;left:29px;top:405px;width:188px;height:188px;border-radius:50%;
  background:radial-gradient(circle at 50% 55%,#e2a64a 0%,#b7742d 55%,#8a5a2a 100%);border:3px solid #fff}
.sauce-note{position:absolute;left:232px;top:440px;font-size:13px;line-height:1.7;color:#fff;font-family:"Shippori Mincho",serif;white-space:nowrap;text-shadow:0 0 4px rgba(60,40,10,.8)}
.feature-label{position:absolute;left:232px;top:600px;font-size:17px;font-weight:500;color:var(--ink)}
.feature-spec{position:absolute;left:232px;top:628px;font-size:11px;line-height:1.5;color:var(--muted)}
.method{position:absolute;right:62px;top:405px;height:300px;writing-mode:vertical-rl;font-family:"Shippori Mincho",serif;font-size:16px;line-height:2;color:var(--ink);letter-spacing:.1em}
.product{position:absolute;top:722px;width:360px}
.product--jam{left:43px}
.product--mini{left:446px}
.product-photo{width:360px;height:232px}
.product--jam .product-photo{background:linear-gradient(160deg,#3a2a18 0%,#7a5523 45%,#d9a13a 75%,#2b1e10 100%)}
.product--mini .product-photo{background:linear-gradient(160deg,#f3efe8 0%,#c64a2b 40%,#e7a63a 65%,#f1ece4 100%)}
.product-label{margin-top:12px;font-size:15px;font-weight:500}
.product-spec{margin-top:6px;font-size:10.5px;line-height:1.55;color:var(--muted)}
.footer{position:absolute;left:40px;right:40px;top:1118px;border-top:1px solid var(--rule);padding-top:14px;display:flex;align-items:baseline;gap:24px;font-size:11px;color:var(--muted)}
.footer .company{font-family:"Shippori Mincho",serif;font-size:17px;font-weight:600;color:var(--ink)}
</style>
</head>
<body>
<main class="flyer">
  <div class="hero-photo" role="img" aria-label="マンゴーソースとパッションフルーツソースの瓶2本、背景に黒いギフト箱"></div>
  <div class="gift-word">Gift</div>
  <h1 class="headline"><span>宝石のような</span><span>トロピカルジャム</span></h1>

  <div class="sauce-photo" role="img" aria-label="フルーツソースをかけたパンケーキ"></div>
  <p class="sauce-note">北海道産てんさい糖と宮崎県産<br>フルーツのみを煮詰めたこだわりのソース</p>
  <h2 class="feature-label">こはるフルーツソース2本セット</h2>
  <p class="feature-spec">内容：マンゴーソース 145g<br>パッションフルーツソース 145g</p>

  <p class="method">真空低温調理法により、酸化の少ない<br>色鮮やかなジャムに仕上げました。</p>

  <section class="product product--jam">
    <div class="product-photo" role="img" aria-label="箱に並んだジャム瓶6個のギフトセット"></div>
    <h3 class="product-label">こはるフルーツジャム6個セット</h3>
    <p class="product-spec">内容：各150g　マンゴージャム／日向夏マーマレード<br>きんかんマーマレード／パイナップルジャム<br>ブルーベリージャム／パパイアジャム</p>
  </section>

  <section class="product product--mini">
    <div class="product-photo" role="img" aria-label="箱に並んだミニジャム瓶6個のギフトセット"></div>
    <h3 class="product-label">こはるフルーツミニジャム6個セット</h3>
    <p class="product-spec">内容：各50g　マンゴージャム／日向夏マーマレード<br>きんかんマーマレード／パイナップルジャム<br>ブルーベリージャム／パパイアジャム</p>
  </section>

  <footer class="footer">
    <span class="company">桐原白浜果樹株式会社</span>
    <span>〒876-2231 宮崎県宮崎市桜丘町岩瀬2264番地</span>
    <span>TEL 0985-47-2291</span>
    <span>FAX 0985-47-3356</span>
  </footer>
</main>
</body>
</html>
```